Stationary Design Foundation Repair Business

We need business card and letterhead design for foundation repair business. Design must compliment the supplied logo. Font is eurostyle. please feel free to ask any questions. Also if we could incorporate the KTL file into the design, but keep the size of it small. Personal details are located in the stationary file.
Updates
I just uploaded a business card design that i like. Just so you guys know what my taste is. Is it possible to create something like this with my business card?
Target Market(s)
Home owners, Builders, Building surveyors, Insurance companies
Industry/Entity Type
Business
Other font styles liked:
- eurostile extended / bold
Look and feel
Each slider illustrates characteristics of the customer's brand and the style your logo design should communicate.

```html
<!DOCTYPE html>
<html lang="en">
<head>
<meta charset="utf-8">
<title>Bedrock Level Stationery</title>
<link href="https://fonts.googleapis.com/css2?family=Michroma&family=Play:wght@400;700&display=swap" rel="stylesheet">
<style>
:root{
  --red:#c4161c;
  --ink:#1a1a1a;
  --card:#1d1e22;
  --paper:#ffffff;
  --faint-light:#ebebeb;
  --faint-dark:#4b4c51;
  --muted:#9a9a9a;
  --bg-top:#7a7a7a;
  --bg-bottom:#575757;
}
*{margin:0;padding:0;box-sizing:border-box}
html,body{width:1200px;height:1000px;overflow:hidden}
body{background:linear-gradient(135deg,var(--bg-top),var(--bg-bottom));position:relative;font-family:"Play",sans-serif;color:var(--ink)}
.sheet{position:absolute;overflow:hidden;box-shadow:0 2px 6px rgba(0,0,0,.35)}
.letterhead{left:35px;top:25px;width:490px;height:695px;background:var(--paper)}
.envelope{left:600px;top:82px;width:525px;height:248px;background:var(--paper)}
.card{width:294px;height:182px;background:var(--card);color:#fff}
.abs{position:absolute}
.brand{position:absolute;display:flex;align-items:center;gap:6px;font-family:"Michroma",sans-serif;white-space:nowrap;letter-spacing:.3px}
.brand-mark{display:inline-block;background:var(--red)}
.abn{position:absolute;font-family:"Play",sans-serif;white-space:nowrap}
.contacts{position:absolute;list-style:none}
.contacts li{display:flex;align-items:center;gap:5px;white-space:nowrap;line-height:1.35}
.contacts .icon{flex:none;background:var(--red);border-radius:1px;position:relative}
.contacts .icon::after{content:"";position:absolute;left:25%;top:25%;width:50%;height:50%;border-radius:50%;background:#fff}
.contacts .indent{padding-left:12px}
.badge{position:absolute;display:flex;align-items:center;gap:5px;font-family:"Play",sans-serif;font-weight:700;white-space:nowrap}
.badge-seal{flex:none;border-radius:50%;border:2px solid currentColor;opacity:.85}
.faint-name{position:absolute;font-family:"Michroma",sans-serif;white-space:nowrap;text-align:center}
.wave{position:absolute;left:0;bottom:0;display:block}
.holder{position:absolute;font-family:"Michroma",sans-serif}
.holder-role{font-family:"Play",sans-serif;color:#cfcfcf}
.web-accent{color:var(--red)}
</style>
</head>
<body>

<!-- Letterhead -->
<section class="sheet letterhead">
  <div class="brand" style="left:33px;top:40px;font-size:15px;color:var(--ink)"><span class="brand-mark" style="width:12px;height:12px"></span>BEDROCK LEVEL</div>
  <div class="abn" style="left:186px;top:66px;font-size:9px">ABN: 12 345 678 901</div>
  <div class="badge" style="left:365px;top:18px;font-size:11px;color:var(--ink)"><span class="badge-seal" style="width:22px;height:22px"></span>KTL</div>
  <ul class="contacts" style="left:364px;top:47px;font-size:8px">
    <li><span class="icon" style="width:6px;height:6px"></span>0400 123 456</li>
    <li><span class="icon" style="width:6px;height:6px"></span>info@bedrocklevel.com.au</li>
    <li><span class="icon" style="width:6px;height:6px"></span>www.bedrocklevel.com.au</li>
    <li><span class="icon" style="width:6px;height:6px"></span>12 Karoo Lane Eastfield</li>
    <li class="indent">Vic 3900</li>
  </ul>
  <div class="faint-name" style="left:0;width:490px;top:370px;font-size:30px;color:var(--faint-light)">BEDROCK LEVEL</div>
  <svg class="wave" width="490" height="70" viewBox="0 0 490 70" preserveAspectRatio="none">
    <path d="M0,2 C140,28 300,44 490,26 L490,70 L0,70 Z" fill="#111"/>
    <path d="M0,7 C140,33 300,49 490,31 L490,70 L0,70 Z" fill="var(--red)"/>
  </svg>
</section>

<!-- Envelope -->
<section class="sheet envelope">
  <div class="brand" style="left:36px;top:42px;font-size:15px;color:var(--ink)"><span class="brand-mark" style="width:12px;height:12px"></span>BEDROCK LEVEL</div>
  <div class="abn" style="left:196px;top:69px;font-size:9px">ABN: 12 345 678 901</div>
  <ul class="contacts" style="left:42px;top:95px;font-size:8px">
    <li><span class="icon" style="width:6px;height:6px"></span>0400 123 456</li>
    <li><span class="icon" style="width:6px;height:6px"></span>info@bedrocklevel.com.au</li>
    <li><span class="icon" style="width:6px;height:6px"></span>www.bedrocklevel.com.au</li>
    <li><span class="icon" style="width:6px;height:6px"></span>12 Karoo Lane Eastfield</li>
    <li class="indent">Vic 3900</li>
  </ul>
  <div class="badge" style="left:46px;top:146px;font-size:11px;color:var(--ink)"><span class="badge-seal" style="width:20px;height:20px"></span>KTL</div>
  <div class="faint-name" style="left:190px;width:240px;top:145px;font-size:20px;color:var(--faint-light)">BEDROCK LEVEL</div>
  <svg class="wave" width="525" height="70" viewBox="0 0 525 70" preserveAspectRatio="none">
    <path d="M0,2 C150,38 320,52 525,18 L525,70 L0,70 Z" fill="#111"/>
    <path d="M0,7 C150,43 320,57 525,23 L525,70 L0,70 Z" fill="var(--red)"/>
  </svg>
</section>

<!-- Business card front, plain -->
<section class="sheet card" style="left:558px;top:393px">
  <div class="holder" style="left:28px;top:40px;font-size:11px">Marcus Elwin<div class="holder-role" style="font-size:7px;margin-top:3px">Proprietor</div></div>
  <ul class="contacts" style="left:28px;top:106px;font-size:8px;color:#fff">
    <li><span class="icon" style="width:6px;height:6px"></span>612.555.0147</li>
    <li><span class="icon" style="width:6px;height:6px"></span>info@bedrocklevel.com.au</li>
    <li><span class="icon" style="width:6px;height:6px"></span>www.<span class="web-accent">bedrocklevel</span>.com.au</li>
    <li><span class="icon" style="width:6px;height:6px"></span>12 Karoo Lane Eastfield</li>
    <li class="indent">Vic 3900</li>
  </ul>
  <div class="brand" style="left:166px;top:134px;font-size:8.5px;color:#fff"><span class="brand-mark" style="width:8px;height:8px"></span>BEDROCK LEVEL</div>
  <div class="abn" style="left:162px;top:152px;font-size:8.5px;color:#fff">ABN: 12 345 678 901</div>
</section>

<!-- Business card back, plain -->
<section class="sheet card" style="left:873px;top:393px">
  <div class="faint-name" style="left:0;width:294px;top:52px;font-size:30px;color:var(--faint-dark)">BEDROCK</div>
  <div class="badge" style="left:170px;top:138px;font-size:12px;color:#fff"><span class="badge-seal" style="width:24px;height:24px"></span>KTL</div>
</section>

<!-- Business card front, wave -->
<section class="sheet card" style="left:558px;top:597px">
  <div class="holder" style="left:28px;top:32px;font-size:11px">Marcus Elwin<div class="holder-role" style="font-size:7px;margin-top:3px">Proprietor</div></div>
  <ul class="contacts" style="left:28px;top:84px;font-size:8px;color:#fff">
    <li><span class="icon" style="width:6px;height:6px"></span>612.555.0147</li>
    <li><span class="icon" style="width:6px;height:6px"></span>info@bedrocklevel.com.au</li>
    <li><span class="icon" style="width:6px;height:6px"></span>www.<span class="web-accent">bedrocklevel</span>.com.au</li>
    <li><span class="icon" style="width:6px;height:6px"></span>12 Karoo Lane Eastfield</li>
    <li class="indent">Vic 3900</li>
  </ul>
  <div class="brand" style="left:160px;top:118px;font-size:8.5px;color:#fff"><span class="brand-mark" style="width:8px;height:8px"></span>BEDROCK LEVEL</div>
  <svg class="wave" width="294" height="48" viewBox="0 0 294 48" preserveAspectRatio="none">
    <path d="M0,2 C80,30 180,38 294,12 L294,48 L0,48 Z" fill="#fff"/>
    <path d="M0,6 C80,34 180,42 294,16 L294,48 L0,48 Z" fill="var(--red)"/>
  </svg>
</section>

<!-- Business card back, wave -->
<section class="sheet card" style="left:873px;top:602px">
  <div class="faint-name" style="left:0;width:294px;top:42px;font-size:26px;color:var(--faint-dark)">BEDROCK</div>
  <div class="abn" style="left:44px;top:138px;font-size:8.5px;color:#fff">ABN: 12 345 678 901</div>
  <div class="badge" style="left:148px;top:128px;font-size:12px;color:#fff"><span class="badge-seal" style="width:24px;height:24px"></span>KTL</div>
  <svg class="wave" width="294" height="42" viewBox="0 0 294 42" preserveAspectRatio="none">
    <path d="M0,4 C90,34 190,36 294,8 L294,42 L0,42 Z" fill="#fff"/>
    <path d="M0,8 C90,38 190,40 294,12 L294,42 L0,42 Z" fill="var(--red)"/>
  </svg>
</section>

<!-- Business card back, wave, large mark -->
<section class="sheet card" style="left:873px;top:807px">
  <div class="faint-name" style="left:0;width:294px;top:34px;font-size:38px;color:var(--faint-dark)">BEDROCK</div>
  <div class="abn" style="left:44px;top:138px;font-size:8.5px;color:#fff">ABN: 12 345 678 901</div>
  <div class="badge" style="left:148px;top:128px;font-size:12px;color:#fff"><span class="badge-seal" style="width:24px;height:24px"></span>KTL</div>
  <svg class="wave" width="294" height="42" viewBox="0 0 294 42" preserveAspectRatio="none">
    <path d="M0,4 C90,34 190,36 294,8 L294,42 L0,42 Z" fill="#fff"/>
    <path d="M0,8 C90,38 190,40 294,12 L294,42 L0,42 Z" fill="var(--red)"/>
  </svg>
</section>

</body>
</html>
```